Ravel Oversight Partners - Statonery Design

I just completed a redesign of my business card. Please do not design a logo or business card. See my current stationery design attached.

Target Market(s)

VP of Human Resources and Finance - Companies with 100 employees to 10,000

Industry/Entity Type

Business Consultant

Requirements
Must have
• Use the letterhead instructions for the color and fonts.

```html
<!DOCTYPE html>
<html lang="en">
<head>
<meta charset="utf-8">
<title>Ravel Oversight Partners – Stationery</title>
<link href="https://fonts.googleapis.com/css2?family=Bodoni+Moda:wght@400&family=Mulish:wght@400;600&family=Lato:wght@400&display=swap" rel="stylesheet">
<style>
  :root{
    --maroon:#6b1f45;
    --slate:#636166;
    --ink:#2e2e2e;
    --paper:#ffffff;
    --stage:#ffffff;
    --serif:'Bodoni Moda', 'Didot', serif;
    --sans:'Mulish', 'Helvetica Neue', sans-serif;
  }
  html,body{margin:0;padding:0;width:1200px;height:1026px;overflow:hidden;background:var(--stage);}
  .stage{position:relative;width:1200px;height:1026px;font-family:var(--sans);color:var(--ink);}
  .sheet{position:absolute;background:var(--paper);box-shadow:0 0 0 1px #ececec;}
  .brand{position:absolute;display:flex;align-items:center;gap:12px;}
  .brand-dot{width:68px;height:68px;border-radius:50%;background:var(--maroon);flex:none;}
  .brand-name{font-family:var(--serif);font-weight:400;font-size:24px;line-height:26px;color:var(--slate);}
  .contact{position:absolute;border-left:1.5px solid #555;padding-left:22px;font-size:8.5px;line-height:11px;letter-spacing:.3px;color:var(--ink);}
  .contact .row{display:flex;align-items:center;gap:4px;}
  .contact svg{width:7px;height:7px;}
  /* letterhead */
  .letterhead{left:49px;top:33px;width:509px;height:658px;}
  .letter{position:absolute;left:29px;top:162px;width:450px;font-size:10px;line-height:13.5px;letter-spacing:.2px;}
  .letter p{margin:0;}
  .letter .to{margin-top:22px;}
  .letter .salute{margin-top:40px;}
  .letter .body{margin-top:8px;text-align:justify;line-height:15px;}
  .letter .body-serif{font-family:var(--serif);font-size:9.5px;text-align:justify;line-height:14.5px;}
  .letter .closing{margin-top:30px;}
  .letter .signer{margin-top:30px;color:var(--maroon);font-weight:600;font-size:11.5px;}
  /* envelope with address */
  .card{left:582px;top:33px;width:569px;height:248px;}
  /* envelope flap */
  .envelope{left:49px;top:714px;width:569px;height:248px;}
  .flap{position:absolute;left:0;top:0;}
  .flap-name{position:absolute;left:0;right:0;top:24px;text-align:center;font-family:var(--serif);font-size:22px;color:#fff;}
  .values{position:absolute;left:0;right:0;text-align:center;font-family:'Lato',sans-serif;font-size:11.5px;letter-spacing:.6px;}
  .values .bar{color:var(--maroon);margin:0 12px;}
  .envelope .values{top:204px;color:var(--slate);}
  /* folder */
  .folder{left:642px;top:302px;width:509px;height:660px;background:var(--slate);box-shadow:none;}
  .spine{position:absolute;left:0;top:0;width:65px;height:100%;background:var(--maroon);border-right:3px solid #fff;}
  .folder-dot{position:absolute;left:257px;top:273px;width:62px;height:62px;border-radius:50%;background:var(--maroon);}
  .folder-name{position:absolute;left:65px;right:-40px;top:340px;text-align:center;font-family:var(--serif);font-size:25px;color:#fff;}
  .folder .values{left:65px;right:-40px;top:612px;color:#fff;}
  .folder .values .bar{color:#9c3a68;}
</style>
</head>
<body>
<div class="stage">

  <section class="sheet letterhead">
    <div class="brand" style="left:29px;top:30px;">
      <span class="brand-dot"></span>
      <span class="brand-name">Ravel Oversight<br>Partners</span>
    </div>
    <div class="contact" style="left:333px;top:39px;height:50px;">
      <div>418 Linden Street NE</div>
      <div>Suite 210, Fairhaven</div>
      <div>MI 49622</div>
      <div class="row"><svg viewBox="0 0 10 10"><path d="M2 1l2 2-1 1.5c.6 1.2 1.3 1.9 2.5 2.5L7 6l2 2-1.5 1.5C4.5 9 1 5.5.5 2.5z" fill="var(--maroon)"/></svg>555.214.7730</div>
      <div class="row"><svg viewBox="0 0 10 10"><circle cx="5" cy="5" r="4.5" fill="var(--maroon)"/></svg>www.raveloversight.com</div>
    </div>
    <div class="letter">
      <p>Date: 20 November 2018</p>
      <p class="to">To<br>Hollowmere Nursery Ltd.<br>48 Briar Close, Suite# B<br>Leeds, UK LS4 7QA</p>
      <p class="salute">Dear Smith,</p>
      <p class="body">Lorem Ipsum is simply dummy text of the printing and typesetting industry. Lorem Ipsum has been the industry's standard dummy text ever since the 1500s, when an unknown printer took a galley of type and scrambled it to make a type specimen book. It has survived not only five centuries, but also the leap into electronic typesetting, remaining essentially unchanged. It was popularised in the 1960s with the release of Marlowe sheets containing Lorem Ipsum passages, and more recently with desktop publishing software like Quillset Composer including versions of Lorem Ipsum.</p>
      <p class="body-serif">Lorem Ipsum is simply dummy text of the printing and typesetting industry. Lorem Ipsum has been the industry's.</p>
      <p class="closing">Thanking you</p>
      <p class="signer">Daniel Mercer</p>
      <p>CMCA</p>
    </div>
  </section>

  <section class="sheet card">
    <div class="brand" style="left:29px;top:30px;">
      <span class="brand-dot"></span>
      <span class="brand-name">Ravel Oversight<br>Partners</span>
    </div>
    <div class="contact" style="left:29px;top:160px;height:52px;">
      <div>418 Linden Street NE</div>
      <div>Suite 210, Fairhaven</div>
      <div>MI 49622</div>
      <div class="row"><svg viewBox="0 0 10 10"><path d="M2 1l2 2-1 1.5c.6 1.2 1.3 1.9 2.5 2.5L7 6l2 2-1.5 1.5C4.5 9 1 5.5.5 2.5z" fill="var(--maroon)"/></svg>555.214.7730</div>
      <div class="row"><svg viewBox="0 0 10 10"><circle cx="5" cy="5" r="4.5" fill="var(--maroon)"/></svg>www.raveloversight.com</div>
    </div>
  </section>

  <section class="sheet envelope">
    <svg class="flap" width="569" height="76" viewBox="0 0 569 76">
      <path d="M0 0H569L546 55Q537 76 515 76H54Q32 76 23 55Z" fill="var(--maroon)"/>
    </svg>
    <div class="flap-name">Ravel Oversight Partners</div>
    <div class="values">INTEGRITY<span class="bar">|</span>DILIGENCE<span class="bar">|</span>EXCELLENCE</div>
  </section>

  <section class="sheet folder">
    <div class="spine"></div>
    <div class="folder-dot"></div>
    <div class="folder-name">Ravel Oversight Partners</div>
    <div class="values">INTEGRITY<span class="bar">|</span>DILIGENCE<span class="bar">|</span>EXCELLENCE</div>
  </section>

</div>
</body>
</html>
```